Custom Monogramming and Retail gifts

We need a Business Card for a monogramming business that offers many retail gift options. We are a home based business that uses social media (Chatterbox,clipboardia and our website) to sell our products. Our target market is college age, high school, baby gifts.
We want a preppy fun look. Monogramming is very popular in the South

Industry/Entity Type

College

Contact Information for Business Card

Threadwell Keepsakes
Custom Monogramming and Gifts
7152 Brackenway Lane
Willowmere, XA 30999
Della Marsh, Owner
555-314-2790
threadwellkeepsakes.example
threadwellkeepsakes@mailbox.example

```html
<!DOCTYPE html>
<html lang="en">
<head>
<meta charset="utf-8">
<title>Threadwell Keepsakes — Business Card</title>
<link rel="stylesheet" href="https://fonts.googleapis.com/css2?family=Great+Vibes&family=Cormorant+Garamond:wght@500;600&display=swap">
<style>
  :root {
    --backdrop: #d9d9d9;
    --card-white: #ffffff;
    --ink: #161616;
    --panel-dark: #1c1c1c;
    --pink: #e8247d;
    --stitch: #ffffff;
    --text-light: #f4f4f4;
    --script: "Great Vibes", cursive;
    --serif: "Cormorant Garamond", serif;
  }
  * { margin: 0; padding: 0; box-sizing: border-box; }
  html, body {
    width: 1200px; height: 900px; overflow: hidden;
    background: var(--backdrop);
  }
  .canvas { position: relative; width: 1200px; height: 900px; }
  .business-card {
    position: absolute; left: 75px; top: 150px;
    width: 1050px; height: 600px;
    border-radius: 42px; overflow: hidden;
    background: var(--card-white);
    box-shadow: 0 14px 30px rgba(0,0,0,0.18);
  }
  .card-shapes { position: absolute; inset: 0; }
  .brand {
    position: absolute; left: 20px; top: 120px; width: 440px;
    text-align: center;
  }
  .brand-name {
    font-family: var(--script);
    color: var(--pink);
    font-size: 76px; line-height: 0.98; font-weight: 400;
  }
  .tagline-label {
    display: inline-block; margin-top: 30px;
    background: var(--ink); color: var(--text-light);
    font-family: var(--script); font-size: 36px; line-height: 1.2;
    white-space: nowrap;
    padding: 10px 34px 12px;
    border-radius: 12px;
    outline: 2px dashed var(--stitch); outline-offset: -8px;
  }
  .contact {
    position: absolute; left: 600px; top: 0; width: 440px; height: 600px;
    color: var(--text-light); font-family: var(--serif);
    text-align: center;
  }
  .owner-name {
    position: absolute; top: 78px; left: 0; width: 440px;
    font-family: var(--script); color: var(--pink);
    font-size: 54px; line-height: 1;
  }
  .owner-title {
    position: absolute; top: 136px; left: 0; width: 440px;
    font-size: 22px; font-weight: 600;
  }
  .details {
    position: absolute; top: 300px; left: 0; width: 440px;
    font-size: 24px; line-height: 1.35; font-weight: 500;
  }
  .details .phone { font-size: 28px; margin-bottom: 4px; }
  .social {
    position: absolute; right: 10px; bottom: 48px;
    display: flex; gap: 18px;
    font-size: 19px; font-weight: 600;
  }
  .social-item { display: flex; align-items: center; gap: 6px; }
  .social-square {
    width: 18px; height: 18px; background: var(--pink); border-radius: 3px;
  }
</style>
</head>
<body>
<main class="canvas">
  <section class="business-card">
    <svg class="card-shapes" viewBox="0 0 1050 600" width="1050" height="600">
      <path class="accent-band" d="M500 0 Q455 320 530 600 L600 600 L665 0 Z" fill="var(--pink)"/>
      <path class="dark-panel" role="img" aria-label="Black panel with a subtle damask pattern"
            d="M650 0 Q560 250 545 600 L1050 600 L1050 0 Z" fill="var(--panel-dark)"/>
      <path class="stitch-line" d="M675 0 Q587 255 572 600" fill="none"
            stroke="var(--stitch)" stroke-width="2.5" stroke-dasharray="9 7"/>
    </svg>

    <div class="brand">
      <div class="brand-name">Threadwell<br>Keepsakes</div>
      <div class="tagline-label">Custom Monogramming</div>
    </div>

    <div class="contact">
      <div class="owner-name">Della Marsh</div>
      <div class="owner-title">Owner</div>
      <div class="details">
        <div class="phone">555-314-2790</div>
        <div>threadwellkeepsakes.example</div>
        <div>threadwellkeepsakes@mailbox.example</div>
        <div>7152 Brackenway Lane Willowmere,</div>
        <div>XA 30999</div>
      </div>
      <div class="social">
        <span class="social-item"><span class="social-square"></span>Chatterbox</span>
        <span class="social-item"><span class="social-square"></span>clipboardia</span>
      </div>
    </div>
  </section>
</main>
</body>
</html>
```